A billboard for Pine Hollow Construction size 36.5’ x 14.5’

Hi guys. We are purchasing a billboard and are looking for a design (size 36.5’ x 14.5’). Our slogan is "Quality you deserve, service you can count on". The goal of this billboard is brand recognition primarily letting people know we do roofs. Attached are logos that can be used if needed. Not necessarily all of them need to be used.

Target Market(s)

Residents in the local areas needing or thinking about a roof replacement

Industry/Entity Type

Roofing

Requirements
Must have
• Logo and services (roof replacement, gutters, siding, and snow removal)
Nice to have
• take a look at our website for ideas www.pinehollowconstruction.example

```html
<!DOCTYPE html>
<html lang="en">
<head>
<meta charset="utf-8">
<title>Pine Hollow Construction – Billboard</title>
<link rel="stylesheet" href="https://fonts.googleapis.com/css2?family=Montserrat:wght@500;700;900&family=Playfair+Display:wght@400&display=swap">
<style>
  :root {
    --backdrop: #2e2e2e;
    --white: #ffffff;
    --red: #ff0000;
    --ink: #111111;
    --badge-blue: #1d5c86;
    --badge-blue-dark: #164a6d;
    --badge-red: #c8102e;
    --badge-dark: #2b2b2b;
    --badge-grey: #a3a3a3;
  }
  * { box-sizing: border-box; margin: 0; padding: 0; }
  html, body { width: 1044px; height: 1200px; overflow: hidden; }
  body {
    background: var(--backdrop);
    display: flex; align-items: center; justify-content: center;
    font-family: "Montserrat", Arial, sans-serif;
  }
  .billboard {
    position: relative;
    width: 980px; height: 378px;
    background: var(--white);
    box-shadow: 0 20px 50px rgba(0,0,0,.5);
    overflow: hidden;
  }

  /* photo band */
  .photo-band { position: absolute; left: 0; top: 0; width: 100%; height: 175px; }
  .photo { position: absolute; top: 0; height: 100%; width: 440px; }
  .photo--cabin {
    left: 0;
    background:
      radial-gradient(ellipse 170px 90px at 330px 10px, rgba(74,104,52,.95), rgba(74,104,52,0) 100%),
      radial-gradient(ellipse 90px 80px at 200px 95px, rgba(196,140,78,.95), rgba(196,140,78,0) 100%),
      linear-gradient(170deg, #8b8376 0%, #7a6f60 35%, #6b5d4c 65%, #85776a 100%);
  }
  .photo--house {
    right: 0;
    background:
      radial-gradient(ellipse 220px 110px at 260px 120px, rgba(196,204,200,.95), rgba(196,204,200,0) 100%),
      radial-gradient(ellipse 160px 60px at 250px 40px, rgba(86,98,112,.9), rgba(86,98,112,0) 100%),
      linear-gradient(180deg, #b9c9dc 0%, #d9dfe4 25%, #8f9aa4 60%, #aeb5b4 100%);
  }
  .logo-panel { position: absolute; left: 0; top: 0; width: 100%; height: 100%; }
  .brand {
    position: absolute; left: 340px; top: 92px; width: 320px;
    text-align: center;
    font-family: "Playfair Display", Georgia, serif;
    font-weight: 400; font-size: 31px; line-height: 32px;
    color: var(--ink);
  }

  /* headline */
  .headline-band {
    position: absolute; left: 0; top: 175px; width: 100%; height: 121px;
    background: var(--red);
    display: flex; align-items: center; justify-content: center;
  }
  .headline {
    color: var(--white);
    font-weight: 900; font-size: 57px; line-height: 53px;
    text-align: center; white-space: nowrap;
  }

  /* services */
  .services-label {
    position: absolute; left: 0; top: 305px;
    width: 203px; height: 22px;
    background: var(--ink); color: var(--white);
    border-radius: 0 11px 11px 0;
    font-weight: 900; font-size: 17px; line-height: 22px;
    padding-left: 34px; white-space: nowrap;
  }
  .service {
    position: absolute;
    font-weight: 500; font-size: 16px; line-height: 19px; color: var(--ink);
    white-space: nowrap; list-style: none;
  }
  .service--bullet::before {
    content: ""; position: absolute; left: -15px; top: 7px;
    width: 6px; height: 6px; border-radius: 50%; background: var(--red);
  }
  .row-1 { top: 332px; }
  .row-2 { top: 351px; }

  /* badges */
  .badge { position: absolute; }
  .badge--accredit {
    left: 624px; top: 315px; width: 131px; height: 49px; border-radius: 4px;
    background: linear-gradient(90deg, var(--white) 0 34%, var(--badge-blue) 34% 100%);
    border: 2px solid var(--badge-blue);
  }
  .badge--shingle { left: 786px; top: 310px; width: 54px; height: 56px; border-radius: 50%; background: var(--badge-red); }
  .badge--guard { left: 846px; top: 333px; width: 33px; height: 33px; background: var(--badge-dark); }
  .badge--select { left: 904px; top: 311px; width: 54px; height: 56px; border-radius: 4px; background: var(--badge-grey); }
</style>
</head>
<body>
  <main class="billboard">
    <section class="photo-band">
      <div class="photo photo--cabin" role="img" aria-label="Photo of a timber-framed house with a shingled roof and trees behind"></div>
      <div class="photo photo--house" role="img" aria-label="Photo of a grey two-storey house with a new slate-blue shingle roof"></div>
      <svg class="logo-panel" viewBox="0 0 980 175" preserveAspectRatio="none" aria-hidden="true">
        <polygon points="396,0 604,0 706,175 288,175" fill="#ffffff"/>
      </svg>
      <p class="brand">Pine Hollow<br>Construction</p>
    </section>

    <section class="headline-band">
      <h1 class="headline">QUALITY YOU DESERVE,<br>SERVICE YOU CAN COUNT ON</h1>
    </section>

    <h2 class="services-label">OUR SERVICES:</h2>
    <ul class="services">
      <li class="service service--bullet row-1" style="left:40px;">Residential &amp; Commercial</li>
      <li class="service row-2" style="left:40px;">Roof Replacement</li>
      <li class="service service--bullet row-1" style="left:285px;">Roof Repairs</li>
      <li class="service service--bullet row-2" style="left:285px;">New Construction</li>
      <li class="service service--bullet row-1" style="left:428px;">Gutters</li>
      <li class="service service--bullet row-1" style="left:532px;">Siding</li>
      <li class="service service--bullet row-2" style="left:477px;">Snow Removal</li>
    </ul>

    <div class="badge badge--accredit" role="img" aria-label="Business accreditation badge"></div>
    <div class="badge badge--shingle" role="img" aria-label="Shingle manufacturer badge"></div>
    <div class="badge badge--guard" role="img" aria-label="Roof protection partner badge"></div>
    <div class="badge badge--select" role="img" aria-label="Certified installer badge"></div>
  </main>
</body>
</html>
```